Irrigation Business needs their business cards modernised and revamped

I would like to keep my current logo, colours and revamp the format of the card.

I would like the card to be clean yet important.

Im not sure if you include texture but i would like the named logo to be indented into the card etc.

show me something alive and free something thats clinical to the point yet has a feel of achievement. i would like people to go nice card.

Target Market(s)

high end clients, corporate, sports field manger, the guys that make the decisions

Industry/Entity Type

Business

Contact Information for Business Card

nformation to be included

Gareth Minchin (Director)
0472958316
gareth@tkwater.biz
www.tomskerrywatering.com

instagram logo
google logo
facebook logo

Colors

Designer to choose colors to be used in the design.

Requirements
Nice to have
• indentations a really nice feel to the card good texture

```html
<!DOCTYPE html>
<html lang="en">
<head>
<meta charset="utf-8">
<title>Tom's Kerry Watering – Business Card</title>
<link rel="stylesheet" href="https://fonts.googleapis.com/css2?family=Oswald:wght@500&family=Open+Sans:wght@400;700&display=swap">
<style>
  :root {
    --backdrop: #1b1b1d;
    --card-white: #f4f4f4;
    --brand-blue: #2f62a6;
    --brand-navy: #1f4f93;
    --ink-white: #ffffff;
    --ink-soft: rgba(255,255,255,0.85);
  }
  * { margin: 0; padding: 0; box-sizing: border-box; }
  html, body { width: 1200px; height: 904px; overflow: hidden; }
  body {
    background: var(--backdrop);
    font-family: "Open Sans", sans-serif;
    position: relative;
  }
  .card {
    position: absolute;
    width: 560px;
    height: 320px;
    border-radius: 2px;
    box-shadow: 0 18px 40px rgba(0,0,0,0.55);
  }
  .card-front {
    left: 80px; top: 90px;
    background: linear-gradient(135deg, #ffffff 0%, var(--card-white) 60%, #e6e6e6 100%);
    display: flex; align-items: center; justify-content: center; gap: 16px;
  }
  .brand-mark {
    width: 58px; height: 58px; border-radius: 50%;
    background: var(--brand-blue);
    flex: none;
  }
  .brand-name {
    font-family: "Open Sans", sans-serif;
    font-weight: 700;
    font-size: 27px;
    letter-spacing: 0.5px;
    color: var(--brand-navy);
    text-transform: uppercase;
  }
  .card-back {
    left: 560px; top: 494px;
    background: var(--brand-blue);
    color: var(--ink-white);
  }
  .identity {
    position: absolute; right: 258px; top: 106px;
    text-align: right;
    white-space: nowrap;
  }
  .person-name {
    font-family: "Oswald", sans-serif;
    font-weight: 500;
    font-size: 38px;
    line-height: 1;
    text-transform: uppercase;
    letter-spacing: -0.5px;
  }
  .person-role {
    font-size: 13px;
    line-height: 1.3;
    color: var(--ink-soft);
    margin-top: 4px;
  }
  .divider {
    position: absolute; left: 318px; top: 96px;
    width: 1px; height: 82px;
    background: var(--ink-soft);
  }
  .contact-list {
    position: absolute; left: 334px; top: 100px;
    list-style: none;
  }
  .contact-list li {
    display: flex; align-items: center; gap: 8px;
    font-size: 13px; line-height: 25px;
    white-space: nowrap;
  }
  .contact-list svg { width: 13px; height: 13px; flex: none; }
  .social-row {
    position: absolute; left: 334px; top: 244px;
    display: flex; gap: 12px;
  }
  .social-slot {
    width: 26px; height: 26px;
    border: 2px solid var(--ink-white);
    border-radius: 5px;
  }
</style>
</head>
<body>
  <section class="card card-front" aria-label="Card front">
    <span class="brand-mark" aria-hidden="true"></span>
    <span class="brand-name">Tom's Kerry Watering</span>
  </section>

  <section class="card card-back" aria-label="Card back">
    <div class="identity">
      <p class="person-name">Gareth Minchin</p>
      <p class="person-role">Director</p>
    </div>
    <span class="divider" aria-hidden="true"></span>
    <ul class="contact-list">
      <li>
        <svg viewBox="0 0 16 16" aria-hidden="true"><path d="M3 1.5l3 3-1.6 1.8c.8 1.9 2.4 3.5 4.3 4.3L10.5 9l3 3-2 2C6 14 2 10 1.5 3.5z" fill="none" stroke="#fff" stroke-width="1.4" stroke-linejoin="round"/></svg>
        0472958316
      </li>
      <li>
        <svg viewBox="0 0 16 16" aria-hidden="true"><rect x="1.5" y="3.5" width="13" height="9" fill="none" stroke="#fff" stroke-width="1.4"/><path d="M1.5 3.5L8 9l6.5-5.5" fill="none" stroke="#fff" stroke-width="1.4"/></svg>
        gareth@tkwater.biz
      </li>
      <li>
        <svg viewBox="0 0 16 16" aria-hidden="true"><circle cx="8" cy="8" r="6.3" fill="none" stroke="#fff" stroke-width="1.4"/><ellipse cx="8" cy="8" rx="2.8" ry="6.3" fill="none" stroke="#fff" stroke-width="1.2"/><path d="M1.7 8h12.6" stroke="#fff" stroke-width="1.2"/></svg>
        www.tomskerrywatering.com
      </li>
    </ul>
    <div class="social-row" aria-label="Social media">
      <span class="social-slot"></span>
      <span class="social-slot"></span>
      <span class="social-slot"></span>
    </div>
  </section>
</body>
</html>
```